KLT Website Homepage Redesign

My website needs a homepage redesign and banner photos updates for Discovery and SEO Services pages. We sell Search Engine Optimization services. We use Search Engine Optimization techniques to help our clients rank high in search engines like Zorvix. It is an intense competition to consistently rank above other businesses. The problem is there is no easy way to show what the benefits of Search Engine Optimization services look like in an emotional way. I want to use an image from sailboat racing to dramatize that our clients win at Search Engine Optimization marketing.
The following products are desired:
1. Desktop version homepage redesign with a banner that clearly shows we sell Search Engine Optimization services using sailboat racing as a metaphor.
2. Mobile version homepage redesign with a banner that clearly shows we sell Search Engine Optimization services using sailboat racing as a metaphor.
2. New banner photo for the Discovery Page
3. New banner photo for the SEO page
The design must be responsive and show well on desktops, laptops, tablets and mobile phones. The current footer style must be kept. A third service called SEO must be added.
the website URL is www.velmorbix.com
Target Market(s)
Business to Business
Industry/Entity Type
Digital Marketing
Coding
Coded - Design and coding required
Number of Pages Required
1 page
Colors
Designer to choose colors to be used in the design.
Look and feel
Each slider illustrates characteristics of the customer's brand and the style your logo design should communicate.

```html
<!DOCTYPE html>
<html lang="en">
<head>
<meta charset="utf-8">
<title>KLT Applications – Search Engine Optimization</title>
<link href="https://fonts.googleapis.com/css2?family=Fira+Sans:wght@400;500;600&display=swap" rel="stylesheet">
<style>
:root{
  --navy:#1b3a72;
  --heading:#1f3f7c;
  --ink:#1a1a1a;
  --body:#3a3a3a;
  --yellow:#ffcc00;
  --link:#f2a51f;
  --icon-bg:#e4eff4;
  --line:#c9c9c9;
  --field:#f6f6f6;
}
*{margin:0;padding:0;box-sizing:border-box}
html,body{width:1200px;height:4577px;overflow:hidden}
body{font-family:"Fira Sans",sans-serif;color:var(--ink);background:#fff;position:relative}
.abs{position:absolute}
.center{text-align:center}

/* header */
.site-header{position:absolute;top:0;left:0;width:1200px;height:85px;background:#fff;border-bottom:3px solid var(--navy)}
.brand{position:absolute;left:128px;top:22px;font-size:30px;font-weight:500;color:var(--navy);display:flex;align-items:center;gap:10px}
.brand-dot{width:12px;height:12px;border-radius:50%;background:var(--navy)}
.main-nav{position:absolute;top:30px;font-size:15px;font-weight:500;color:var(--ink)}
.search-btn{position:absolute;left:1048px;top:28px;width:27px;height:27px;border-radius:50%;background:var(--yellow);display:flex;align-items:center;justify-content:center}

/* hero */
.hero{position:absolute;top:88px;left:0;width:1200px;height:614px;background:linear-gradient(180deg,#c9d2cf 0%,#e6d8b6 35%,#a9b9b2 55%,#3f8c9a 75%,#1f4f66 100%)}
.hero-title{position:absolute;left:124px;top:160px;font-size:45px;font-weight:600;line-height:52px;color:#111;width:480px}
.hero-sub{position:absolute;left:124px;top:330px;font-size:16px;line-height:25px;color:#1a1a1a;width:430px}
.btn{display:flex;align-items:center;justify-content:center;background:var(--yellow);color:#111;font-weight:600;font-size:16px}
.hero-btn{position:absolute;left:124px;top:404px;width:232px;height:41px}

/* sections */
.section-title{position:absolute;left:0;width:1200px;text-align:center;font-size:35px;font-weight:500;color:#111}
.card-photo{position:absolute;top:889px;width:285px;height:199px}
.card-label{position:absolute;top:1106px;width:300px;text-align:center;font-size:27px;line-height:34px;font-weight:500}

.service{position:absolute;width:300px;text-align:center}
.service .ico{width:89px;height:89px;border-radius:50%;background:var(--icon-bg);margin:0 auto 18px;display:flex;align-items:center;justify-content:center}
.service h3{font-size:21px;font-weight:500;color:var(--heading);margin-bottom:12px}
.service p{font-size:11.5px;line-height:17px;color:var(--body);text-align:left;height:72px}
.service .more{font-size:14px;color:var(--link);margin-top:6px;display:block}

.band{position:absolute;left:0;width:1200px;background:var(--navy);color:#fff}
.audience{position:absolute;top:2488px;font-size:21px;font-weight:500;color:#fff;text-align:center;line-height:26px}
.dot{position:absolute;top:2516px;width:4px;height:4px;border-radius:50%;background:var(--yellow)}

.client-shot{position:absolute;top:2841px;width:292px;height:192px}
.client-name{position:absolute;top:3058px;width:300px;text-align:center;font-size:21px;line-height:26px;font-weight:500}

/* form */
.field-label{position:absolute;font-size:14px;color:var(--body)}
.field-label i{color:var(--link);font-style:normal}
.field{position:absolute;height:48px;background:var(--field);border:1px solid var(--line)}
.captcha{position:absolute;left:868px;top:3901px;width:140px;height:48px;border:1px solid var(--line);background:#fff;display:flex;align-items:center;justify-content:center;font-size:26px;color:#b01e2a;letter-spacing:1px}

/* footer */
.site-footer{position:absolute;top:4177px;left:0;width:1200px;height:400px;background:linear-gradient(180deg,#24447d 0%,#1d3d74 55%,#2b4f86 80%,#1a355f 100%);color:#fff}
.footer-title{position:absolute;left:124px;top:66px;font-size:22px;font-weight:500}
.footer-head{position:absolute;top:122px;font-size:14px;font-weight:500}
.footer-text{position:absolute;font-size:11.5px;line-height:17px}
.footer-links{position:absolute;top:162px;list-style:none;font-size:11.5px;line-height:25px}
.copyright{position:absolute;left:0;top:376px;width:1200px;text-align:center;font-size:10px;color:#e6e6e6}
</style>
</head>
<body>

<header class="site-header">
  <div class="brand"><span class="brand-dot"></span>KLT Applications</div>
  <nav>
    <span class="main-nav" style="left:798px">Info</span>
    <span class="main-nav" style="left:860px">Let’s Talk</span>
    <span class="main-nav" style="left:956px">Support</span>
  </nav>
  <div class="search-btn">
    <svg width="15" height="15" viewBox="0 0 16 16"><circle cx="6.5" cy="6.5" r="5" fill="none" stroke="#fff" stroke-width="1.8"/><line x1="10.2" y1="10.2" x2="14.5" y2="14.5" stroke="#fff" stroke-width="1.8"/></svg>
  </div>
</header>

<section class="hero" role="img" aria-label="Racing sailboats with white sails on a teal sea under a golden cloudy sky">
  <h1 class="hero-title">Win the Search Game with Search Engine Optimization</h1>
  <p class="hero-sub">We Empower Clients with Web Presence That Drives Them Ahead of Competition</p>
  <a class="btn hero-btn">Start Taking the Lead</a>
</section>

<h2 class="section-title" style="top:782px">What We Provide to Up Your Game</h2>
<div class="card-photo" style="left:124px;background:linear-gradient(135deg,#8f8a84,#4b3b30)" role="img" aria-label="Consultant writing notes at a wooden desk"></div>
<div class="card-photo" style="left:459px;background:linear-gradient(135deg,#1c2630,#0b1117);border-bottom:3px solid var(--yellow)" role="img" aria-label="Code on a dark computer screen"></div>
<div class="card-photo" style="left:791px;background:linear-gradient(135deg,#39485a,#6b7f7a)" role="img" aria-label="Man in front of a board with marketing sketches"></div>
<div class="card-label" style="left:116px">SEO Consulting</div>
<div class="card-label" style="left:448px">Website Design, Development &amp; Hosting</div>
<div class="card-label" style="left:792px">SEO (Search Engine Optimization)</div>

<!-- services -->
<div class="service" style="left:390px;top:1261px;width:420px">
  <div class="ico"><svg width="50" height="50" viewBox="0 0 50 50" fill="none" stroke="#1f3f7c" stroke-width="2"><circle cx="21" cy="21" r="14"/><line x1="31" y1="31" x2="44" y2="44" stroke-width="3"/></svg></div>
  <h3>Discovery</h3>
  <p style="text-align:center;height:auto">Understanding your business goals informs the design and development phases, all of which enable your website to do more.</p>
  <span class="more">Learn More →</span>
</div>

<div class="service" style="left:121px;top:1508px">
  <div class="ico"><svg width="46" height="46" viewBox="0 0 46 46" fill="none" stroke="#1f3f7c" stroke-width="2"><rect x="6" y="8" width="34" height="24"/><line x1="23" y1="32" x2="23" y2="38"/><line x1="15" y1="38" x2="31" y2="38"/><circle cx="21" cy="19" r="6"/><line x1="25" y1="23" x2="30" y2="28"/></svg></div>
  <h3>Search Engine Optimization</h3>
  <p>A website built with a strong SEO base is essential. Powerful search engine optimization means higher placement on search engine results pages and more visitors on your website. Everything begins there.</p>
  <span class="more">Learn More →</span>
</div>
<div class="service" style="left:450px;top:1508px">
  <div class="ico"><svg width="46" height="46" viewBox="0 0 46 46" fill="none" stroke="#1f3f7c" stroke-width="2"><rect x="15" y="6" width="16" height="10"/><rect x="4" y="30" width="12" height="9"/><rect x="17" y="30" width="12" height="9"/><rect x="30" y="30" width="12" height="9"/><path d="M23 16v7M10 30v-7h26v7M23 23v7"/></svg></div>
  <h3>Website Strategy</h3>
  <p>A strong company website increases leads and reduces bounces by giving a visitor exactly what they’re looking for and hooks them with both helpfulness and expertise.</p>
  <span class="more">Learn More →</span>
</div>
<div class="service" style="left:780px;top:1508px">
  <div class="ico"><svg width="46" height="46" viewBox="0 0 46 46" fill="none" stroke="#1f3f7c" stroke-width="2"><rect x="5" y="7" width="36" height="26"/><line x1="5" y1="13" x2="41" y2="13"/><line x1="10" y1="19" x2="22" y2="19"/><line x1="10" y1="25" x2="20" y2="25"/><circle cx="31" cy="25" r="6"/><path d="M28 25l2 2 4-4"/><line x1="23" y1="33" x2="23" y2="39"/></svg></div>
  <h3>Local Optimization</h3>
  <p>When online audiences can find businesses in their own backyard to answer all of their needs, your business can win—as long as your web strategy is prepared for these local queries.</p>
  <span class="more">Learn More →</span>
</div>

<div class="service" style="left:121px;top:1773px">
  <div class="ico"><svg width="46" height="46" viewBox="0 0 46 46" fill="none" stroke="#1f3f7c" stroke-width="2"><path d="M12 6h8v26l-4 7-4-7z"/><path d="M26 6h8v26l-4 7-4-7z"/><line x1="12" y1="12" x2="20" y2="12"/><line x1="26" y1="12" x2="34" y2="12"/></svg></div>
  <h3>Web Writing Services</h3>
  <p>Well-crafted web writing is a balancing act between message, brand voice, audience expectation, and SEO. Our experienced writing and editing team is ready when you are.</p>
  <span class="more">Learn More →</span>
</div>
<div class="service" style="left:450px;top:1773px">
  <div class="ico"><svg width="46" height="46" viewBox="0 0 46 46" fill="none" stroke="#1f3f7c" stroke-width="2"><rect x="11" y="5" width="24" height="36" rx="3"/><circle cx="23" cy="22" r="8"/><path d="M23 17v5l3 3"/><line x1="20" y1="37" x2="26" y2="37"/></svg></div>
  <h3>PPC</h3>
  <p>Beyond organic SEO strategies, Pay-Per-Click (PPC) tactics are one more way to get your business in front of your customers’ eyes online, and this is one of our favorite marketing strategies.</p>
  <span class="more">Learn More →</span>
</div>
<div class="service" style="left:780px;top:1773px">
  <div class="ico"><svg width="46" height="46" viewBox="0 0 46 46" fill="none" stroke="#1f3f7c" stroke-width="2"><rect x="8" y="9" width="30" height="21"/><path d="M4 34h38l-3 4H7z"/><circle cx="23" cy="19.5" r="4"/><path d="M23 13v2M23 24v2M16.5 19.5h2M27.5 19.5h2"/></svg></div>
  <h3>Advanced Web Tools</h3>
  <p>CRM or API integration, ecommerce capabilities, advanced calendars and forms—whatever you might need, we can make it happen for you.</p>
  <span class="more">Learn More →</span>
</div>

<div class="service" style="left:450px;top:2038px">
  <div class="ico"><svg width="46" height="46" viewBox="0 0 46 46" fill="none" stroke="#1f3f7c" stroke-width="2"><circle cx="23" cy="23" r="17"/><ellipse cx="23" cy="23" rx="8" ry="17"/><line x1="6" y1="23" x2="40" y2="23"/><path d="M9 14h28M9 32h28"/></svg></div>
  <h3>Hosting &amp; Support</h3>
  <p style="height:56px">A reliable hosting environment is the difference between a website that is fast or slow, vulnerable to attack or secure, backed-up or not.</p>
  <span class="more">Learn More →</span>
</div>

<!-- audiences -->
<section class="band" style="top:2331px;height:295px"></section>
<h2 class="section-title" style="top:2395px;color:#fff">Who Do We Work With?</h2>
<div class="audience" style="left:114px;width:110px;top:2505px">Startups</div>
<div class="dot" style="left:255px"></div>
<div class="audience" style="left:286px;width:170px">Small To<br>Medium-Sized<br>Businesses</div>
<div class="dot" style="left:485px"></div>
<div class="audience" style="left:515px;width:140px;top:2507px">Nonprofits</div>
<div class="dot" style="left:682px"></div>
<div class="audience" style="left:715px;width:150px;top:2492px">Government<br>Agencies</div>
<div class="dot" style="left:896px"></div>
<div class="audience" style="left:930px;width:160px;top:2492px">ECommerce<br>Marketplaces</div>

<!-- clients -->
<h2 class="section-title" style="top:2725px">What Our Clients are Saying</h2>
<div class="client-shot" style="left:124px;background:linear-gradient(180deg,#f2f2f2 0%,#e8e8e8 50%,#9a1d5a 51%,#9a1d5a 55%,#f4f4f4 56%)" role="img" aria-label="Screenshot of the Center for Learner Growth website"></div>
<div class="client-shot" style="left:454px;background:linear-gradient(180deg,#1f5fa8 0%,#1f5fa8 8%,#e9dcd0 9%,#c8b39a 80%,#fff 81%)" role="img" aria-label="Screenshot of the SLDA learning framework website"></div>
<div class="client-shot" style="left:784px;background:linear-gradient(180deg,#ececec 0%,#ececec 24%,#1d3f9a 25%,#2a56b8 90%,#e6e6e6 91%)" role="img" aria-label="Screenshot of the Harborline Medical Care website"></div>
<div class="client-name" style="left:121px">Center for Learner<br>Growth</div>
<div class="client-name" style="left:450px">SLDA</div>
<div class="client-name" style="left:780px">Harborline Medical Care</div>

<!-- cta -->
<section class="band" style="top:3211px;height:277px"></section>
<h2 class="section-title" style="top:3291px;color:#fff">Ready to Start Taking the Lead?</h2>
<a class="btn abs" style="left:484px;top:3357px;width:231px;height:43px;font-size:15px">Contact Us Today</a>

<!-- form -->
<h2 class="section-title" style="top:3567px">Let’s Work Together</h2>
<form>
  <label class="field-label" style="left:124px;top:3662px">First Name<i>*</i></label>
  <label class="field-label" style="left:617px;top:3662px">Last Name<i>*</i></label>
  <div class="field" style="left:124px;top:3695px;width:459px"></div>
  <div class="field" style="left:617px;top:3695px;width:459px"></div>
  <label class="field-label" style="left:124px;top:3765px">Email<i>*</i></label>
  <label class="field-label" style="left:617px;top:3765px">Phone<i>*</i></label>
  <div class="field" style="left:124px;top:3798px;width:459px"></div>
  <div class="field" style="left:617px;top:3798px;width:459px"></div>
  <label class="field-label" style="left:124px;top:3866px">Company Name<i>*</i></label>
  <label class="field-label" style="left:617px;top:3866px">Enter the Captcha</label>
  <div class="field" style="left:124px;top:3901px;width:459px"></div>
  <div class="field" style="left:617px;top:3901px;width:229px"></div>
  <div class="captcha">dhe58n</div>
  <svg class="abs" style="left:1028px;top:3913px" width="24" height="24" viewBox="0 0 24 24" fill="none" stroke="#666" stroke-width="2.5"><path d="M19 12a7 7 0 1 1-3-5.7"/><path d="M17 2v5h-5" stroke-width="2"/></svg>
  <a class="btn abs" style="left:484px;top:4004px;width:231px;height:43px;font-size:15px">Submit</a>
</form>

<!-- footer -->
<footer class="site-footer" role="img" aria-label="Sailboats on the water beneath a navy overlay">
  <div class="footer-title">Take the Lead</div>
  <div class="footer-head" style="left:124px">Contact Us</div>
  <p class="footer-text" style="left:124px;top:152px">2418 Harbor Crest Way<br>Suite 210<br>Bayport, MD 21990</p>
  <div class="footer-head" style="left:601px">Useful Links</div>
  <ul class="footer-links" style="left:601px"><li>Home</li><li>Web Strategy</li><li>Support</li><li>Privacy</li></ul>
  <ul class="footer-links" style="left:839px"><li>SEO</li><li>Advanced Website Tools</li><li>Testimonials</li><li>Terms of Use</li></ul>
  <p class="copyright">© 2020 KLT Applications | All Rights Reserved | Web Strategy by KLT Applications</p>
</footer>

</body>
</html>
```